Business Card design for Property Developer

We need a business card design for a Melbourne based Property Developer called "Kestrelmoor Holdings Pty Ltd".

We subdivide land and onsell to builders etc.

We already have a company logo, which is attached. Also I have attached the layout requirements from the printer. We would like a 2-sided design with one side displaying our logo by itself and the other with the required info, such as name, address, tel no., email, abn etc. The card will need to be used by 4 members of staff so name and contact details should be interchangable.
Updates

If possible, can you please write "name' "job position" "phone" "email" "address" on the card but leave them so I can add the details at a later time. Thank you. Also I plan on printing with UV spot printing as a background on the card. Keep this is mind when designing.

Thanks again.

Hello designers, please do not include pics of houses, house plansĀ or construction machinery etc as we really do not like the way it looks. Thank you.

Target Market(s)

Real Estate Agents, Land Owners, Local Council Departments, Govt Bodies, other Developers etc.

Industry/Entity Type

Business

Requirements
Must have
• 2-sided design with one side displaying our logo by itself and the other with the required info, such as name, address, tel no., email, abn etc.

```html
<!DOCTYPE html>
<html lang="en">
<head>
<meta charset="utf-8">
<title>Kestrelmoor Holdings – Business Card</title>
<link rel="stylesheet" href="https://fonts.googleapis.com/css2?family=Open+Sans:ital,wght@0,700;1,400;1,700&display=swap">
<style>
  :root {
    --page-bg: #d9d9d9;
    --card-blue: #233e95;
    --card-ink: #ffffff;
    --card-shadow: rgba(0, 0, 0, 0.25);
  }
  html, body {
    margin: 0;
    padding: 0;
    width: 1200px;
    height: 1000px;
    overflow: hidden;
    background: var(--page-bg);
    font-family: "Open Sans", Verdana, sans-serif;
  }
  .sheet {
    width: 1200px;
    height: 1000px;
    display: flex;
    flex-direction: column;
    align-items: center;
    justify-content: center;
    gap: 80px;
  }
  .card {
    position: relative;
    width: 840px;
    height: 300px;
    background: var(--card-blue);
    color: var(--card-ink);
    box-shadow: 0 6px 18px var(--card-shadow);
    box-sizing: border-box;
  }
  .card--info {
    display: flex;
    align-items: center;
    padding: 0 70px;
  }
  .contact {
    font-style: italic;
    font-size: 24px;
    line-height: 33px;
    letter-spacing: 0.5px;
    word-spacing: 3px;
    text-align: right;
    white-space: nowrap;
  }
  .contact p { margin: 0; }
  .contact .email { text-align: left; }
  .person {
    margin-left: 70px;
    text-align: center;
    font-style: italic;
    margin-top: -30px;
  }
  .person__name {
    margin: 0;
    font-weight: 700;
    font-size: 24px;
    letter-spacing: 0.5px;
  }
  .person__role {
    margin: 2px 0 0;
    font-size: 20px;
  }
  .card--brand {
    display: flex;
    align-items: center;
    padding-left: 110px;
  }
  .brand {
    display: flex;
    align-items: center;
    gap: 18px;
  }
  .brand__mark {
    width: 56px;
    height: 56px;
    border-radius: 50%;
    background: var(--card-ink);
  }
  .brand__name {
    font-weight: 700;
    font-style: normal;
    font-size: 34px;
    line-height: 1.15;
    letter-spacing: 1px;
    text-transform: uppercase;
    color: var(--card-ink);
  }
</style>
</head>
<body>
  <main class="sheet">
    <section class="card card--info" aria-label="Card front: contact details">
      <div class="contact">
        <p>418 Larkspur Parade, #212</p>
        <p>Carrowvale, VC 30417-2281</p>
        <p>tel. 5391 7026 / 6482 1957 fax.</p>
        <p>5617 3049 / 8256 4718</p>
        <p class="email">dalton@kestrelmoor-holdings.com</p>
      </div>
      <div class="person">
        <p class="person__name">DALTON WHITLOCK</p>
        <p class="person__role">manager</p>
      </div>
    </section>

    <section class="card card--brand" aria-label="Card back: company name">
      <div class="brand">
        <span class="brand__mark"></span>
        <span class="brand__name">Kestrelmoor<br>Holdings</span>
      </div>
    </section>
  </main>
</body>
</html>
```